Smart, intuitive SaaS software dashboard design

PactLoom is an innovative modern SaaS (software as a service) solution for contract and meeting management.

What we are looking for is fresh ideas for our dashboard. We do not need web coding or actionable wireframes now – but purely great design ideas from where to continue forward.

How should a modern web software dashboard look like? Fresh, intuitive, easy-to-use, and adaptable for responsive mobile designs. We hope that when the user logs into the service and sees the dashboard, he/she gets a good big picture of the current status of the most important documents of his/hers company.

To get to know the service and see the components, we kindly ask you to register to our service at www.pactloom-example.net and to utilize the free trial (30 days) so you can see the existing dashboard live. And also try out how it works. Might help you to get ideas how to improve it.

(The designer we will choose might be offered later on to design some other pages as well (contract view and edit pages, meeting page etc).)

You’ll find additional information in the attachment.

You’ll find more information of the company and the service also at www.pactloom-example.net

Target Market(s)

Global

Industry/Entity Type

Business Management

Number of Pages Required

1 page

Font styles to use
Sans Serif

Requirements
Must have
• 1) Clear design idea for us to iterate from, 2) Modern look and feel - elegant & bold at the same time - still with credibility in our target group. And 3) Suitable for dashboard usage - it should it a clear big picture for the user.
• UPDATE:
• Users should see most important things with one glance. Therefore we would like to see AT LEAST these items mentioned below on the first page.
• NOTE: if all these things are visible on the dashboard, the menu list is maybe not needed on the left. (And there might be some icons on the top header with needed settings/inbox features anyway.)
• NOTE2: as explained earlier, the design should be responsive i.e. work without modifications in PC, iPad and mobile (the areas/boxes would just rearrange themselves on top of each other.)
• -First area should be Documents, which would include different document categories: Contracts, Finance & Admin and HR
• -All different types of Meetings could be the next area (upcoming ones clearly visible with date and maybe description, time and location visible also).
• -Reminders and Activity Feed (they might also be together in top of each other, so that Reminder is visible first and Activity feed can be chosen from the tab.)
• -Virtual Datarooms (maybe 1-3 different ones with some analytics for each visible e.g. like usage/visits per day)
• Saved searches in very important list as users can save their most important searches. There are typically many of these, so at least 5 should be visible and then see all button (maybe even more could be visible if they fit on your design)
• My Latest is also important.
• (As explained, Action Required area is NOT needed anymore).
Nice to have
• Surprise us!
Should not have
• Please avoid the boring traditional legacy stuff and the common report dashboards.
• You do not need design a 100% mockup for the techie to continue with. The ideas count.

```html
<!DOCTYPE html>
<html lang="en">
<head>
<meta charset="utf-8">
<title>PactLoom Dashboard</title>
<link href="https://fonts.googleapis.com/css2?family=Roboto:wght@400;500;700&display=swap" rel="stylesheet">
<style>
:root{
  --green:#7acc00;
  --dark:#1b1b1b;
  --btn:#333333;
  --page:#f0f0f0;
  --panel:#f9f9f9;
  --white:#ffffff;
  --line:#e3e3e3;
  --text:#2b2b2b;
  --muted:#8a8a8a;
  --soft:#b5b5b5;
}
*{box-sizing:border-box;margin:0;padding:0}
html,body{width:1159px;height:1200px;overflow:hidden}
body{background:var(--page);font-family:"Roboto",Arial,sans-serif;color:var(--text);position:relative}
svg{display:block}

/* header */
.topbar{position:absolute;left:0;top:0;width:1159px;height:77px;background:var(--dark)}
.brand{position:absolute;left:26px;top:18px;display:flex;align-items:center;gap:10px;color:var(--white);font-size:24px;font-weight:500;letter-spacing:.5px}
.brand-dot{width:36px;height:36px;border-radius:50%;background:var(--green)}
.search{position:absolute;left:269px;top:20px;width:323px;height:36px;border-radius:18px;background:var(--white);overflow:hidden;display:flex}
.search-input{flex:1;padding-left:16px;line-height:36px;font-size:13px;color:var(--soft)}
.search-scope{width:108px;background:var(--green);color:var(--white);font-size:13px;font-weight:500;line-height:36px;padding-left:16px;display:flex;align-items:center;gap:12px}
.add-btn{position:absolute;left:612px;top:20px;width:36px;height:36px;border:2px solid var(--green);border-radius:50%}
.icon-btn{position:absolute;top:26px}
.badge{position:absolute;top:-7px;right:-9px;width:15px;height:15px;border-radius:50%;background:var(--green);color:var(--white);font-size:9px;font-weight:700;text-align:center;line-height:15px}
.divider-v{position:absolute;top:0;width:1px;height:77px;background:#333}
.user{position:absolute;left:833px;top:18px;display:flex;align-items:center;gap:12px;color:#ddd;font-size:13px;font-weight:500}
.avatar{width:42px;height:42px;border-radius:50%;background:linear-gradient(135deg,#6d6d6d,#2e2e2e);border:2px solid #555}
.help{position:absolute;left:1033px;top:28px;color:var(--white);font-size:14px;font-weight:700}
.logout{position:absolute;left:1112px;top:31px}

/* panels */
.panel{position:absolute;background:var(--panel);border:1px solid #e6e6e6}
.panel-head{height:41px;background:var(--green);color:var(--white);font-size:16px;font-weight:500;line-height:41px;padding-left:21px}
.btn-dark{position:absolute;background:var(--btn);color:var(--white);font-size:12px;font-weight:500;height:28px;line-height:28px;padding:0 16px;display:flex;align-items:center;gap:7px}

/* documents */
.doc-row{position:absolute;left:26px;width:759px;height:78px;border-bottom:1px solid var(--line)}
.doc-icon{position:absolute;left:30px;top:24px}
.doc-sep{position:absolute;left:57px;top:18px;width:1px;height:40px;background:var(--line)}
.doc-title{position:absolute;left:74px;top:24px;font-size:14.5px}
.doc-cat{position:absolute;left:74px;top:47px;font-size:11px;color:#555}
.doc-sep2{position:absolute;left:433px;top:18px;width:1px;height:40px;background:var(--line)}
.doc-stats{position:absolute;left:460px;top:23px;font-size:12px;color:var(--soft);display:flex;gap:6px;align-items:center}
.doc-date{position:absolute;left:460px;top:46px;font-size:11px;color:var(--soft)}

/* meetings */
.meet-row{position:absolute;left:26px;width:759px;height:110px;border-bottom:1px solid var(--line)}
.date-box{position:absolute;left:0;top:14px;width:58px;height:67px;background:var(--white)}
.date-num{font-size:36px;text-align:center;line-height:50px;color:#222}
.date-month{height:17px;background:var(--green);color:var(--white);font-size:11px;text-align:center;line-height:17px}
.meet-title{position:absolute;left:75px;top:14px;font-size:14.5px}
.meet-desc{position:absolute;left:75px;top:34px;width:500px;font-size:11px;line-height:15px;color:#666}
.meet-meta{position:absolute;left:75px;top:70px;font-size:12px;color:var(--soft);display:flex;gap:8px;align-items:center}
.meet-sep{position:absolute;left:647px;top:13px;width:1px;height:72px;background:var(--line)}
.meet-actions{position:absolute;left:680px;top:42px;display:flex;gap:17px}

/* side tabs */
.tabs{display:flex;height:41px;background:var(--page)}
.tab{padding:0 23px;line-height:38px;font-size:12.5px;color:var(--soft);background:#e9e9e9;margin-right:6px}
.tab.active{background:var(--white);color:var(--text);border-top:3px solid var(--green);line-height:38px}
.timeline{position:absolute;left:29px;top:56px;width:1px;height:351px;background:var(--line)}
.rem{position:absolute;left:24px;width:240px}
.rem-dot{position:absolute;left:0;top:24px;width:10px;height:10px;border-radius:50%;background:var(--green)}
.rem-date{position:absolute;left:26px;top:0;font-size:12.5px;color:var(--soft)}
.rem-text{position:absolute;left:26px;top:20px;font-size:11px;line-height:15px;color:#555}
.rem.current .rem-date{color:var(--text)}
.rem.current .rem-text{color:var(--green);text-decoration:underline}
.latest{position:absolute;left:0;width:297px;height:78px;border-bottom:1px solid var(--line)}
.latest.current{background:var(--white);width:298px}
.latest-tick{position:absolute;left:25px;top:30px}
.latest-text{position:absolute;left:50px;top:22px;font-size:12px;line-height:17px;color:#555}

/* footer */
.footer{position:absolute;left:0;top:1132px;width:1159px;height:68px;background:var(--dark)}
.copy{position:absolute;left:26px;top:27px;font-size:12px;color:#999}
.social{position:absolute;left:837px;top:22px;display:flex;gap:8px}
.social span{width:25px;height:25px;border-radius:50%}
.seal{position:absolute;left:1063px;top:18px;width:62px;height:30px;border-radius:4px;background:#f0c419}
</style>
</head>
<body>

<header class="topbar">
  <div class="brand"><span class="brand-dot"></span>PactLoom</div>
  <div class="search">
    <div class="search-input">Search ...</div>
    <div class="search-scope">Contracts
      <svg width="8" height="6" viewBox="0 0 8 6"><path d="M1 1l3 3 3-3" stroke="#fff" stroke-width="1.6" fill="none"/></svg>
    </div>
  </div>
  <div class="add-btn">
    <svg width="32" height="32" viewBox="0 0 32 32"><path d="M16 10v12M10 16h12" stroke="#7acc00" stroke-width="3"/></svg>
  </div>
  <div class="icon-btn" style="left:693px">
    <svg width="20" height="18" viewBox="0 0 20 18" fill="#9a9a9a"><circle cx="7" cy="6" r="3.5"/><circle cx="14" cy="5" r="3"/><path d="M0 17c0-5 3-7 7-7s7 2 7 7z"/><path d="M13 9c4 0 7 2 7 6h-5c-.5-2-1-4-2-6z"/></svg>
    <span class="badge">3</span>
  </div>
  <div class="icon-btn" style="left:743px">
    <svg width="17" height="18" viewBox="0 0 17 18" fill="#9a9a9a"><path d="M8.5 1c3.5 0 5.5 2.5 5.5 6v4l2 3H1l2-3V7c0-3.5 2-6 5.5-6z"/><circle cx="8.5" cy="16" r="2"/></svg>
    <span class="badge">7</span>
  </div>
  <span class="divider-v" style="left:809px"></span>
  <div class="user"><span class="avatar" role="img" aria-label="User profile photo"></span>Marcus Hale</div>
  <span class="divider-v" style="left:1000px"></span>
  <div class="help">?</div>
  <span class="divider-v" style="left:1078px"></span>
  <div class="logout">
    <svg width="14" height="14" viewBox="0 0 14 14" fill="#fff"><path d="M0 1h6v2H2v8h4v2H0z"/><path d="M8 3l5 4-5 4V8.5H4v-3h4z"/></svg>
  </div>
</header>

<!-- Documents -->
<section class="panel" style="left:26px;top:103px;width:783px;height:419px">
  <div class="panel-head">Documents</div>
</section>
<div class="doc-row" style="left:53px;top:147px;width:732px">
  <svg class="doc-icon" width="26" height="32" viewBox="0 0 26 32"><path d="M1 1h17l7 7v23H1z" fill="none" stroke="#b0b0b0" stroke-width="2"/><text x="13" y="24" font-size="13" font-family="Roboto,sans-serif" font-weight="700" fill="#b0b0b0" text-anchor="middle">W</text></svg>
  <span class="doc-sep"></span>
  <div class="doc-title">Agreement Trio 2015-10-11.dox</div>
  <div class="doc-cat">- Contracts</div>
  <span class="doc-sep2"></span>
  <div class="doc-stats">▦ Total: 154, &nbsp;⧗ Starred 42, &nbsp;↻ In Progress 7</div>
  <div class="doc-date">Date Modified: 27-06-2016, 14:27, &nbsp;Size: 437 KB</div>
</div>
<div class="doc-row" style="left:53px;top:225px;width:732px">
  <svg class="doc-icon" width="26" height="32" viewBox="0 0 26 32"><path d="M1 1h17l7 7v23H1z" fill="none" stroke="#b0b0b0" stroke-width="2"/><path d="M7 25c3-4 5-9 6-14 1 5 3 10 7 12-5-1-9 0-13 2z" fill="none" stroke="#b0b0b0" stroke-width="1.5"/></svg>
  <span class="doc-sep"></span>
  <div class="doc-title">Agreement Trio 2015-10-11.pdf</div>
  <div class="doc-cat">- Fina@admin</div>
  <span class="doc-sep2"></span>
  <div class="doc-stats">▦ Total: 154, &nbsp;⧗ Starred 42, &nbsp;↻ In Progress 7</div>
  <div class="doc-date">Date Modified: 27-06-2016, 14:27, &nbsp;Size: 437 KB</div>
</div>
<div class="doc-row" style="left:53px;top:303px;width:732px">
  <svg class="doc-icon" width="26" height="32" viewBox="0 0 26 32"><path d="M1 1h17l7 7v23H1z" fill="none" stroke="#b0b0b0" stroke-width="2"/><text x="13" y="24" font-size="13" font-family="Roboto,sans-serif" font-weight="700" fill="#b0b0b0" text-anchor="middle">W</text></svg>
  <span class="doc-sep"></span>
  <div class="doc-title">Agreement Trio 2015-10-11.dox</div>
  <div class="doc-cat">- HR</div>
  <span class="doc-sep2"></span>
  <div class="doc-stats">▦ Total: 154, &nbsp;⧗ Starred 42, &nbsp;↻ In Progress 7</div>
  <div class="doc-date">Date Modified: 27-06-2016, 14:27, &nbsp;Size: 437 KB</div>
</div>
<div class="doc-row" style="left:53px;top:381px;width:732px;border-bottom:none">
  <svg class="doc-icon" width="26" height="32" viewBox="0 0 26 32"><path d="M1 1h17l7 7v23H1z" fill="none" stroke="#b0b0b0" stroke-width="2"/><path d="M5 26l6-8 4 5 3-3 4 6z" fill="#b0b0b0"/><circle cx="9" cy="12" r="2.5" fill="#b0b0b0"/></svg>
  <span class="doc-sep"></span>
  <div class="doc-title">Agreement Trio 2015-10-11.jpg</div>
  <div class="doc-cat">- Contracts</div>
  <span class="doc-sep2"></span>
  <div class="doc-stats">▦ Total: 154, &nbsp;⧗ Starred 42, &nbsp;↻ In Progress 7</div>
  <div class="doc-date">Date Modified: 27-06-2016, 14:27, &nbsp;Size: 437 KB</div>
</div>
<div class="btn-dark" style="left:53px;top:468px;width:102px;justify-content:center">Show All</div>

<!-- Meetings -->
<section class="panel" style="left:26px;top:550px;width:783px;height:554px">
  <div class="panel-head">Upcoming Meetings</div>
</section>

<div class="meet-row" style="left:52px;top:602px;width:733px">
  <div class="date-box"><div class="date-num">15</div><div class="date-month">January</div></div>
  <div class="meet-title">Board Meeting</div>
  <div class="meet-desc">It is a long established fact that a reader will be distracted by the readable content of a page when looking at its layout. The point of using Lorem Ipsum is that ...</div>
  <div class="meet-meta">◷ 11 A.M &nbsp;/&nbsp; ⚲ Meeting Location</div>
  <span class="meet-sep"></span>
  <div class="meet-actions">
    <svg width="13" height="14" viewBox="0 0 13 14" fill="none" stroke="#aaa" stroke-width="1.4"><path d="M1 3h11M4 3V1h5v2M2.5 3l1 10h6l1-10"/></svg>
    <svg width="16" height="14" viewBox="0 0 16 14" fill="none" stroke="#aaa" stroke-width="1.4"><path d="M10 2H1v11h11V7"/><path d="M6 9l1-3 7-5 1 1-7 5z"/></svg>
  </div>
</div>
<div class="meet-row" style="left:52px;top:712px;width:733px">
  <div class="date-box"><div class="date-num">16</div><div class="date-month">January</div></div>
  <div class="meet-title">Board Meeting</div>
  <div class="meet-desc">It is a long established fact that a reader will be distracted by the readable content of a page when looking at its layout. The point of using Lorem Ipsum is that ...</div>
  <div class="meet-meta">◷ 11 A.M &nbsp;/&nbsp; ⚲ Meeting Location</div>
  <span class="meet-sep"></span>
  <div class="meet-actions">
    <svg width="13" height="14" viewBox="0 0 13 14" fill="none" stroke="#aaa" stroke-width="1.4"><path d="M1 3h11M4 3V1h5v2M2.5 3l1 10h6l1-10"/></svg>
    <svg width="16" height="14" viewBox="0 0 16 14" fill="none" stroke="#7acc00" stroke-width="1.4"><path d="M10 2H1v11h11V7"/><path d="M6 9l1-3 7-5 1 1-7 5z"/></svg>
  </div>
</div>
<div class="meet-row" style="left:52px;top:822px;width:733px">
  <div class="date-box"><div class="date-num">18</div><div class="date-month">January</div></div>
  <div class="meet-title">Shareholder's Meeting</div>
  <div class="meet-desc">It is a long established fact that a reader will be distracted by the readable content of a page when looking at its layout. The point of using Lorem Ipsum is that ...</div>
  <div class="meet-meta">◷ 11 A.M &nbsp;/&nbsp; ⚲ Meeting Location</div>
  <span class="meet-sep"></span>
  <div class="meet-actions">
    <svg width="13" height="14" viewBox="0 0 13 14" fill="none" stroke="#aaa" stroke-width="1.4"><path d="M1 3h11M4 3V1h5v2M2.5 3l1 10h6l1-10"/></svg>
    <svg width="16" height="14" viewBox="0 0 16 14" fill="none" stroke="#aaa" stroke-width="1.4"><path d="M10 2H1v11h11V7"/><path d="M6 9l1-3 7-5 1 1-7 5z"/></svg>
  </div>
</div>
<div class="meet-row" style="left:52px;top:932px;width:733px;border-bottom:none">
  <div class="date-box"><div class="date-num">23</div><div class="date-month">January</div></div>
  <div class="meet-title">Board Meeting</div>
  <div class="meet-desc">It is a long established fact that a reader will be distracted by the readable content of a page when looking at its layout. The point of using Lorem Ipsum is that ...</div>
  <div class="meet-meta">◷ 11 A.M &nbsp;/&nbsp; ⚲ Meeting Location</div>
  <span class="meet-sep"></span>
  <div class="meet-actions">
    <svg width="13" height="14" viewBox="0 0 13 14" fill="none" stroke="#aaa" stroke-width="1.4"><path d="M1 3h11M4 3V1h5v2M2.5 3l1 10h6l1-10"/></svg>
    <svg width="16" height="14" viewBox="0 0 16 14" fill="none" stroke="#aaa" stroke-width="1.4"><path d="M10 2H1v11h11V7"/><path d="M6 9l1-3 7-5 1 1-7 5z"/></svg>
  </div>
</div>
<div class="btn-dark" style="left:51px;top:1051px;width:103px;justify-content:center">Show All</div>

<!-- Reminders -->
<section class="panel" style="left:836px;top:103px;width:297px;height:483px;background:var(--panel)">
  <div class="tabs"><div class="tab active">Reminders</div><div class="tab">Activity Feed</div></div>
  <span class="timeline"></span>
  <div class="rem" style="top:60px"><span class="rem-dot"></span><div class="rem-date">29.62016</div><div class="rem-text">Vivamus finibus diam in feugiat gravida.<br>Sed dapibus</div></div>
  <div class="rem" style="top:128px"><span class="rem-dot"></span><div class="rem-date">29.62016</div><div class="rem-text">Section 1.10.32 of "de Finibus<br>Bonorum et Malorum</div></div>
  <div class="rem current" style="top:196px"><span class="rem-dot"></span><div class="rem-date">29.62016</div><div class="rem-text">Vivamus finibus diam in feugiat gravida.<br>Sed dapibus</div></div>
  <div class="rem" style="top:264px"><span class="rem-dot"></span><div class="rem-date">29.62016</div><div class="rem-text">Section 1.10.32 of "de Finibus<br>Bonorum et Malorum</div></div>
  <div class="rem" style="top:332px"><span class="rem-dot"></span><div class="rem-date">29.62016</div><div class="rem-text">Vivamus finibus diam in feugiat gravida.<br>Sed dapibus</div></div>
  <div class="btn-dark" style="left:24px;top:430px">
    <svg width="11" height="11" viewBox="0 0 11 11" fill="#fff"><path d="M0 2h11v9H0z M2 0h1.5v3H2z M7.5 0H9v3H7.5z"/></svg>Calendar
  </div>
</section>

<!-- Saved searches / My latest -->
<section class="panel" style="left:836px;top:613px;width:297px;height:491px">
  <div class="tabs"><div class="tab">Saved Searches</div><div class="tab active">My Latest</div></div>
  <div class="latest" style="top:41px"><svg class="latest-tick" width="11" height="9" viewBox="0 0 11 9"><path d="M1 4l3 3 6-6" stroke="#aaa" stroke-width="2" fill="none"/></svg><div class="latest-text">Business consultant<br>agreement Jones &amp; Jones</div></div>
  <div class="latest current" style="top:119px"><svg class="latest-tick" width="11" height="9" viewBox="0 0 11 9"><path d="M1 4l3 3 6-6" stroke="#7acc00" stroke-width="2" fill="none"/></svg><div class="latest-text">Business Agreement<br>Morrison</div></div>
  <div class="latest" style="top:197px"><svg class="latest-tick" width="11" height="9" viewBox="0 0 11 9"><path d="M1 4l3 3 6-6" stroke="#aaa" stroke-width="2" fill="none"/></svg><div class="latest-text">Confidentiality Agreement<br>Jones &amp; Jones</div></div>
  <div class="latest" style="top:275px"><svg class="latest-tick" width="11" height="9" viewBox="0 0 11 9"><path d="M1 4l3 3 6-6" stroke="#aaa" stroke-width="2" fill="none"/></svg><div class="latest-text">Confidentiality Agreement<br>Jones &amp; Jones</div></div>
  <div class="latest" style="top:353px;border-bottom:none"><svg class="latest-tick" width="11" height="9" viewBox="0 0 11 9"><path d="M1 4l3 3 6-6" stroke="#aaa" stroke-width="2" fill="none"/></svg><div class="latest-text">Confidentiality Agreement<br>Jones &amp; Jones</div></div>
  <div class="btn-dark" style="left:20px;top:436px">
    <svg width="11" height="11" viewBox="0 0 11 11" fill="#fff"><path d="M0 2h11v9H0z M2 0h1.5v3H2z M7.5 0H9v3H7.5z"/></svg>Calendar
  </div>
</section>

<footer class="footer">
  <div class="copy">© 2016 PactLoom Ltd. Terms of Use &nbsp;/&nbsp; Privacy</div>
  <div class="social">
    <span style="background:#3b5998"></span>
    <span style="background:#cb2027"></span>
    <span style="background:#1da1f2"></span>
    <span style="background:#e62117"></span>
  </div>
  <div class="seal"></div>
</footer>

</body>
</html>
```